TALL Harborin business card design

We had logo design for New Investment company "Tall Harbor" office in Vietnam, Singapore. We would like to design te card " less is more" simple, humble but give the receiver a strong attention and trust

Ex
Lam Duc Thien
Chairman

Address:
Hanoi Office
The Lotus Court, #B305. Kela road, Ward Phuan 2, District North Sonven. Hanoi
Hochiminh city office
Daravo Commerce Tower, Level 37th. #5 Lo Bang st. District 1. Hochiminh City
Singapore office:
14 Pembury Road #05-02 Pembury Point Singapore 239417

M. .......
E: thien.lam@tallharbor.com.vn
W: www.tallharbor.com

Target Market(s)

Startup, partner....

Industry/Entity Type

Investment

Contact Information for Business Card

Lam Duc Thien
Chairman

Address:
Hanoi Office
Hochiminh city office
Singapore office:
M. .......
W: www.tallharbor.com

Colors

Designer to choose colors to be used in the design.

Requirements
Must have
• Less is more. Simple Humble elegant
Nice to have
• Less color, 2 or 1.
• TALL may have color ,the rest may greyscale

```html
<!DOCTYPE html>
<html lang="en">
<head>
<meta charset="utf-8">
<title>Tall Harbor business card</title>
<link rel="stylesheet" href="https://fonts.googleapis.com/css2?family=Open+Sans:wght@400;600;700&display=swap">
<style>
  :root {
    --brand-blue: #2f7fcf;
    --brand-blue-dark: #1f6bb8;
    --ink-grey: #8a8d91;
    --text-grey: #6d7074;
    --paper: #ffffff;
    --backdrop: #2b2b2d;
  }
  * { box-sizing: border-box; margin: 0; padding: 0; }
  html, body {
    width: 1200px; height: 660px; overflow: hidden;
    background: var(--backdrop);
    font-family: "Open Sans", Arial, sans-serif;
  }
  .stage {
    width: 1200px; height: 660px;
    display: flex; align-items: center; justify-content: center; gap: 40px;
  }
  .card {
    position: relative;
    width: 540px; height: 310px;
    background: var(--paper);
    overflow: hidden;
  }

  /* Back of card: offices */
  .card-back .brand-band {
    position: absolute; left: 0; top: 0; width: 100%; height: 128px;
  }
  .card-back .brand-band svg { position: absolute; inset: 0; }
  .card-back .wordmark {
    position: absolute; left: 0; right: 0; top: 38px;
    text-align: center;
    color: var(--paper);
    font-weight: 700; font-size: 40px; letter-spacing: 1px;
  }
  .offices {
    position: absolute; left: 0; right: 0; top: 140px;
    text-align: center;
  }
  .office-title {
    color: var(--brand-blue);
    font-weight: 700; font-size: 11px; letter-spacing: 0.5px;
    text-transform: uppercase;
    margin-top: 6px;
  }
  .office-address {
    color: var(--text-grey);
    font-size: 10.5px;
    margin-top: 2px;
  }
  .card-back .foot-band {
    position: absolute; left: 0; bottom: 0; width: 100%; height: 30px;
  }

  /* Front of card: person */
  .card-front .wordmark {
    position: absolute; left: 30px; top: 115px; width: 220px;
    text-align: center;
    color: var(--brand-blue);
    font-weight: 700; font-size: 36px; letter-spacing: 1px;
  }
  .card-front .divider {
    position: absolute; left: 270px; top: 40px; width: 1px; height: 200px;
    background: #d5d7da;
  }
  .person {
    position: absolute; left: 292px; top: 70px;
  }
  .person-name {
    color: var(--ink-grey);
    font-weight: 700; font-size: 21px;
  }
  .person-role {
    color: var(--brand-blue);
    font-size: 10px; letter-spacing: 6px;
    text-transform: uppercase;
    margin-top: 2px;
  }
  .contact-list { list-style: none; margin-top: 12px; }
  .contact-item {
    display: flex; align-items: center; gap: 8px;
    color: var(--text-grey);
    font-size: 13px; line-height: 20px;
  }
  .contact-item svg { width: 11px; height: 11px; flex: none; }
  .card-front .foot-band {
    position: absolute; left: 0; bottom: 0; width: 100%; height: 26px;
  }
</style>
</head>
<body>
<main class="stage">

  <section class="card card-back" aria-label="Business card back">
    <div class="brand-band">
      <svg width="540" height="128" viewBox="0 0 540 128" preserveAspectRatio="none">
        <polygon points="0,0 540,0 540,100 0,128" fill="var(--brand-blue)"/>
      </svg>
      <div class="wordmark">Tall Harbor</div>
    </div>
    <div class="offices">
      <p class="office-title">Hanoi Office</p>
      <p class="office-address">The Lotus Court, #B305. Kela road, Ward Phuan 2, District North Sonven. Hanoi</p>
      <p class="office-title">Hochiminh City Office</p>
      <p class="office-address">Daravo Commerce Tower, Level 37th. #5 Lo Bang st. District 1. Hochiminh City</p>
      <p class="office-title">Singapore Office</p>
      <p class="office-address">14 Pembury Road #05-02 Pembury Point Singapore 239417</p>
    </div>
    <svg class="foot-band" width="540" height="30" viewBox="0 0 540 30" preserveAspectRatio="none">
      <polygon points="0,14 540,30 0,30" fill="var(--brand-blue)"/>
    </svg>
  </section>

  <section class="card card-front" aria-label="Business card front">
    <div class="wordmark">Tall Harbor</div>
    <div class="divider"></div>
    <div class="person">
      <p class="person-name">Lam Duc Thien</p>
      <p class="person-role">Chairman</p>
      <ul class="contact-list">
        <li class="contact-item">
          <svg viewBox="0 0 12 12"><rect x="3" y="0.5" width="6" height="11" rx="1" fill="none" stroke="var(--brand-blue)" stroke-width="1.2"/><circle cx="6" cy="9.5" r="0.7" fill="var(--brand-blue)"/></svg>
          0987 210 4635
        </li>
        <li class="contact-item">
          <svg viewBox="0 0 12 12"><rect x="0.5" y="2" width="11" height="8" fill="none" stroke="var(--brand-blue)" stroke-width="1.2"/><polyline points="0.5,2 6,7 11.5,2" fill="none" stroke="var(--brand-blue)" stroke-width="1.2"/></svg>
          thien.lam@tallharbor.com.vn
        </li>
        <li class="contact-item">
          <svg viewBox="0 0 12 12"><circle cx="6" cy="6" r="5.3" fill="none" stroke="var(--brand-blue)" stroke-width="1.1"/><ellipse cx="6" cy="6" rx="2.3" ry="5.3" fill="none" stroke="var(--brand-blue)" stroke-width="1"/><line x1="0.7" y1="6" x2="11.3" y2="6" stroke="var(--brand-blue)" stroke-width="1"/></svg>
          www.tallharbor.com
        </li>
      </ul>
    </div>
    <svg class="foot-band" width="540" height="26" viewBox="0 0 540 26" preserveAspectRatio="none">
      <polygon points="0,12 250,18 246,26 0,26" fill="var(--brand-blue)"/>
      <polygon points="256,18 540,0 540,26 252,26" fill="var(--brand-blue-dark)"/>
    </svg>
  </section>

</main>
</body>
</html>
```